Small Catering Menu

I am looking to make a small menu for catering for my company. I am thinking of a small A5 size booklet which will also have some pictures and the cover needs to be attractive.
Likely to be 8-12 pages depending upon your design (could be less or more). I need 2-3 pages as proposal concept (Cover, inside first page and one menu page) and if we like it we will make the project guaranteed before finishing the rest of the project to add security for the designer.
Pictures will be provided to the designer whose concept is the best as they are too heavy. But use generic photos for now (rather large ones) if possible.
Logo is available and so is the inside text as well as some other tidbits.
I will provide the fonts too to ensure it maintains the corporate integrity that we are following.
Industry/Entity Type
Catering

```html
<!DOCTYPE html>
<html lang="en">
<head>
<meta charset="utf-8">
<title>Harbor Table Catering – The Menu</title>
<link href="https://fonts.googleapis.com/css2?family=Josefin+Sans:wght@600&family=Great+Vibes&display=swap" rel="stylesheet">
<style>
  :root {
    --paper: #efede9;
    --gold: #dca54c;
    --ink: #1c1c1a;
  }
  * { margin: 0; padding: 0; box-sizing: border-box; }
  html, body {
    width: 844px;
    height: 1200px;
    overflow: hidden;
    background: var(--paper);
  }
  .cover {
    position: relative;
    width: 844px;
    height: 1200px;
    background: var(--paper);
  }
  .spine-band {
    position: absolute;
    left: 0;
    top: 0;
    width: 36px;
    height: 1200px;
    background: var(--gold);
  }
  .brand {
    position: absolute;
    left: 36px;
    right: 0;
    top: 500px;
    display: flex;
    align-items: center;
    justify-content: center;
    gap: 22px;
  }
  .brand-dot {
    width: 26px;
    height: 26px;
    border-radius: 50%;
    background: var(--gold);
  }
  .brand-name {
    font-family: "Josefin Sans", sans-serif;
    font-weight: 600;
    font-size: 56px;
    letter-spacing: 3px;
    color: var(--ink);
    text-transform: uppercase;
    line-height: 1;
  }
  .menu-title {
    position: absolute;
    left: 36px;
    right: 0;
    top: 965px;
    text-align: center;
    font-family: "Great Vibes", cursive;
    color: var(--ink);
    line-height: 1;
  }
  .menu-title .article {
    display: block;
    font-size: 58px;
    margin-left: -80px;
  }
  .menu-title .word {
    display: block;
    font-size: 128px;
    margin-top: -22px;
  }
</style>
</head>
<body>
  <main class="cover">
    <div class="spine-band"></div>

    <div class="brand">
      <span class="brand-dot"></span>
      <span class="brand-name">Harbor Table Catering</span>
    </div>

    <h1 class="menu-title">
      <span class="article">the</span>
      <span class="word">Menu</span>
    </h1>
  </main>
</body>
</html>
```